First Aid Training business needs business card design

We would like a double sided business card designed for a first aid training business - Banksia First Aid. We provide first aid training and , WHS (work, health and safety) training.

The attached word document contains the key information we would like on each side of the business card.

Final design needs to be delivered in print ready format, along with the original file.

```html
<!DOCTYPE html>
<html lang="en">
<head>
<meta charset="utf-8">
<title>Banksia First Aid – Business Card</title>
<link rel="stylesheet" href="https://fonts.googleapis.com/css2?family=Montserrat:wght@500;700;800&family=Arimo:wght@400;700&display=swap">
<style>
  :root {
    --bg: #c4c4c4;
    --card-white: #ffffff;
    --card-dark: #2b2b2b;
    --red: #e41e26;
    --ink: #111111;
    --grey: #8a8a8a;
    --mark-dark: #161616;
    --text-light: #ffffff;
  }
  * { margin: 0; padding: 0; box-sizing: border-box; }
  html, body {
    width: 1200px; height: 800px; overflow: hidden;
    background: var(--bg);
  }
  .sheet {
    width: 1200px; height: 800px;
    display: flex; flex-direction: column;
    align-items: center; justify-content: center; gap: 36px;
  }
  .card {
    position: relative;
    width: 620px; height: 354px;
    border-bottom: 4px solid var(--red);
    box-shadow: 0 10px 28px rgba(0,0,0,0.25);
    overflow: hidden;
  }

  /* Front */
  .card--front { background: var(--card-white); }
  .brand {
    position: absolute;
    display: flex; align-items: center; gap: 18px;
    font-family: "Montserrat", sans-serif; font-weight: 800;
    text-transform: uppercase; letter-spacing: 0.04em;
  }
  .brand__dot { border-radius: 50%; flex: none; }
  .card--front .brand { left: 150px; top: 70px; color: var(--ink); font-size: 30px; }
  .card--front .brand__dot { width: 58px; height: 58px; background: var(--red); }
  .divider {
    position: absolute; left: 40px; right: 30px; top: 232px;
    height: 1px; background: var(--red);
  }
  .holder {
    position: absolute; left: 40px; top: 196px;
    font-family: "Montserrat", sans-serif; font-weight: 800;
    font-size: 25px; color: var(--red); letter-spacing: 0.03em;
  }
  .contacts {
    position: absolute; left: 40px; top: 246px;
    list-style: none;
    font-family: "Arimo", sans-serif; font-size: 20px; color: var(--ink);
    line-height: 1.4;
  }
  .contacts li { display: flex; align-items: center; gap: 10px; }
  .contacts svg { width: 18px; height: 18px; flex: none; }
  .website {
    position: absolute; right: 30px; top: 200px;
    font-family: "Arimo", sans-serif; font-size: 18px; color: var(--ink);
  }
  .website span { color: var(--red); }

  /* Back */
  .card--back { background: var(--card-dark); }
  .card--back .brand { left: 110px; top: 58px; color: var(--mark-dark); font-size: 32px; }
  .card--back .brand__dot { width: 84px; height: 84px; background: var(--mark-dark); }
  .pitch {
    position: absolute; left: 0; right: 0; top: 196px;
    text-align: center;
    font-family: "Arimo", sans-serif; color: var(--text-light);
  }
  .pitch__headline { font-size: 20px; letter-spacing: 0.02em; }
  .pitch__benefits { margin-top: 8px; font-size: 17px; color: var(--red); }
  .pitch__benefits .sep { color: var(--grey); margin: 0 6px; }
  .pitch__services { margin-top: 12px; font-size: 20px; letter-spacing: 0.02em; }
  .pitch__services .bar { color: var(--red); margin: 0 10px; }
</style>
</head>
<body>
<main class="sheet">

  <section class="card card--front" aria-label="Business card front">
    <div class="brand">
      <span class="brand__dot"></span>
      <span class="brand__name">Banksia First Aid Training</span>
    </div>
    <p class="holder">LIAM HARPER</p>
    <div class="divider"></div>
    <p class="website"><span>banksiafirstaid</span>.com.au</p>
    <ul class="contacts">
      <li>
        <svg viewBox="0 0 24 24" aria-hidden="true"><path fill="#e41e26" d="M6.6 10.8a15 15 0 0 0 6.6 6.6l2.2-2.2c.3-.3.7-.4 1-.2 1.1.4 2.3.6 3.6.6.6 0 1 .4 1 1V20c0 .6-.4 1-1 1A17 17 0 0 1 3 4c0-.6.4-1 1-1h3.5c.6 0 1 .4 1 1 0 1.3.2 2.5.6 3.6.1.3 0 .7-.2 1z"/></svg>
        0412 555 208
      </li>
      <li>
        <svg viewBox="0 0 24 24" aria-hidden="true"><path fill="#e41e26" d="M2 5h20v14H2z"/><path fill="none" stroke="#fff" stroke-width="1.6" d="M2 5l10 8 10-8"/></svg>
        help@banksiafirstaid.com.au
      </li>
    </ul>
  </section>

  <section class="card card--back" aria-label="Business card back">
    <div class="brand">
      <span class="brand__dot"></span>
      <span class="brand__name">Banksia First Aid Training</span>
    </div>
    <div class="pitch">
      <p class="pitch__headline">ONSITE TRAINING – WE CAN COME TO YOU</p>
      <p class="pitch__benefits"><span class="sep">•</span>Time efficient<span class="sep">•</span>Cost effective<span class="sep">•</span>Minimise downtime for your team</p>
      <p class="pitch__services">FIRST AID TRAINING<span class="bar">|</span>WHS TRAINING</p>
    </div>
  </section>

</main>
</body>
</html>
```